New Business Card Design Project

Target Market(s)

Passing cards out

Industry/Entity Type

Asphalt contractor

Contact Information for Business Card

Ridgefold Paving

Colors
FFC000
F8CF3A
FAE287
FDF2CF
FEFAEE
F0912C
F2A743
F7CA91
FBE8D2
FDF5EE
EE7325
F08F49
F5BC92
FAE3D3
FDF4ED

Requirements
Must have
• Asphalt
Nice to have
• Would like to have 2 pictures on it of equipment

```html
<!DOCTYPE html>
<html lang="en">
<head>
<meta charset="utf-8">
<title>Ridgefold Paving – Business Card</title>
<link href="https://fonts.googleapis.com/css2?family=Lexend:wght@400;600;700&display=swap" rel="stylesheet">
<style>
  :root {
    --page-bg: #eeeeee;
    --card-white: #ffffff;
    --orange-light: #f7941d;
    --orange-deep: #d9602f;
    --amber-accent: #ffc857;
    --ink: #1d1d1b;
    --circle-shade: #ececec;
  }
  * { margin: 0; padding: 0; box-sizing: border-box; }
  html, body { width: 1200px; height: 1200px; overflow: hidden; }
  body {
    background: var(--page-bg);
    font-family: "Lexend", sans-serif;
    color: var(--ink);
    position: relative;
  }
  .card {
    position: absolute;
    left: 139px;
    width: 922px;
    height: 526px;
    overflow: hidden;
    background: var(--card-white);
  }
  .card--front { top: 57px; }
  .card--back { top: 617px; }
  .card-art { position: absolute; inset: 0; width: 922px; height: 526px; }
  .holder-name {
    position: absolute; left: 80px; top: 74px;
    font-size: 35px; font-weight: 700; letter-spacing: 0.2px;
  }
  .holder-role {
    position: absolute; left: 80px; top: 122px;
    font-size: 23px; font-weight: 400;
  }
  .contact-list { position: absolute; left: 78px; top: 188px; list-style: none; }
  .contact-item {
    display: flex; align-items: center; gap: 14px;
    height: 37px; font-size: 25px; font-weight: 400;
  }
  .contact-icon { width: 22px; height: 22px; flex: none; }
  .address {
    position: absolute; left: 78px; top: 412px;
    display: flex; gap: 14px; font-size: 25px; line-height: 36px;
  }
  .address .contact-icon { margin-top: 6px; }
  .brand-name {
    position: absolute;
    display: flex; align-items: center; justify-content: center;
    text-align: center; font-weight: 700; color: var(--ink);
    text-transform: uppercase; line-height: 1.15;
  }
  .card--front .brand-name { left: 564px; top: 134px; width: 300px; height: 300px; font-size: 30px; }
  .card--back .brand-name { left: 259px; top: 61px; width: 404px; height: 404px; font-size: 42px; }
</style>
</head>
<body>

<section class="card card--front" aria-label="Business card front">
  <svg class="card-art" viewBox="0 0 922 526" aria-hidden="true">
    <defs>
      <linearGradient id="orangeFront" x1="0" y1="0" x2="1" y2="1">
        <stop offset="0" stop-color="var(--orange-light)"/>
        <stop offset="1" stop-color="var(--orange-deep)"/>
      </linearGradient>
      <linearGradient id="circleFront" x1="0" y1="0" x2="0" y2="1">
        <stop offset="0" stop-color="#ffffff"/>
        <stop offset="1" stop-color="var(--circle-shade)"/>
      </linearGradient>
    </defs>
    <rect class="side-band" x="560" y="0" width="308" height="284" fill="url(#orangeFront)"/>
    <path class="wave-accent" d="M0,338 C300,320 570,380 740,526 L0,526 Z" fill="var(--amber-accent)"/>
    <path class="wave-main" d="M0,368 C300,346 560,408 711,526 L0,526 Z" fill="url(#orangeFront)"/>
    <circle cx="718" cy="290" r="150" fill="#a0522d"/>
    <circle class="brand-circle" cx="714" cy="284" r="150" fill="url(#circleFront)"/>
  </svg>

  <h1 class="holder-name">YOUR NAME</h1>
  <p class="holder-role">Designation</p>

  <ul class="contact-list">
    <li class="contact-item">
      <svg class="contact-icon" viewBox="0 0 24 24" aria-hidden="true"><path fill="var(--ink)" d="M6.6 10.8a15.1 15.1 0 0 0 6.6 6.6l2.2-2.2a1 1 0 0 1 1-.25 11.4 11.4 0 0 0 3.6.57 1 1 0 0 1 1 1V20a1 1 0 0 1-1 1A17 17 0 0 1 3 4a1 1 0 0 1 1-1h3.5a1 1 0 0 1 1 1c0 1.25.2 2.45.57 3.57a1 1 0 0 1-.25 1z"/><path fill="none" stroke="var(--ink)" stroke-width="1.8" stroke-linecap="round" d="M14 3.5a7 7 0 0 1 6.5 6.5M14 7a3.5 3.5 0 0 1 3 3"/></svg>
      <span>(610) 000-0000</span>
    </li>
    <li class="contact-item">
      <svg class="contact-icon" viewBox="0 0 24 24" aria-hidden="true"><rect x="6.5" y="2" width="11" height="20" rx="2" fill="none" stroke="var(--ink)" stroke-width="2"/><rect x="10" y="18" width="4" height="1.6" fill="var(--ink)"/></svg>
      <span>(610) 000-0000</span>
    </li>
    <li class="contact-item">
      <svg class="contact-icon" viewBox="0 0 24 24" aria-hidden="true"><rect x="2" y="5" width="20" height="14" rx="1.5" fill="var(--ink)"/><path d="M3 6.5 12 13l9-6.5" fill="none" stroke="#fff" stroke-width="1.6"/></svg>
      <span>www.ridgefold-paving.com</span>
    </li>
  </ul>

  <p class="address">
    <svg class="contact-icon" viewBox="0 0 24 24" aria-hidden="true"><path fill="var(--ink)" d="M12 2a7 7 0 0 0-7 7c0 5.2 7 13 7 13s7-7.8 7-13a7 7 0 0 0-7-7zm0 9.5A2.5 2.5 0 1 1 12 6.5a2.5 2.5 0 0 1 0 5z"/></svg>
    <span>0/2 Halden Blvd Suite 0000,<br>Corwin, PA 11111</span>
  </p>

  <div class="brand-name">Ridgefold<br>Paving</div>
</section>

<section class="card card--back" aria-label="Business card back">
  <svg class="card-art" viewBox="0 0 922 526" aria-hidden="true">
    <defs>
      <linearGradient id="orangeBack" x1="0" y1="0" x2="1" y2="1">
        <stop offset="0" stop-color="var(--orange-light)"/>
        <stop offset="1" stop-color="var(--orange-deep)"/>
      </linearGradient>
      <linearGradient id="circleBack" x1="0" y1="0" x2="0" y2="1">
        <stop offset="0" stop-color="#ffffff"/>
        <stop offset="1" stop-color="var(--circle-shade)"/>
      </linearGradient>
    </defs>
    <rect width="922" height="526" fill="url(#orangeBack)"/>
    <circle class="brand-circle" cx="461" cy="263" r="202" fill="url(#circleBack)"/>
  </svg>
  <div class="brand-name">Ridgefold<br>Paving</div>
</section>

</body>
</html>
```